Nutrition product information web site

Nutrition Website (see upload) without Shop function but link to Brixel ASIN number that customer could order from Brixel direct. Content must be easily editable without coding. Web environment must be responsive to support mobile devices as well. design should be modern and clear. loading of web elements must be fast. not too much time consuming features.

Industry/Entity Type

Nutrition

Number of Pages Required

5+ page

Font styles to use
Sans Serif

Colors
33b8a4
9bcb3c
0255a3
0a90cc
a54499

Requirements
Must have
• read attached document
Nice to have
• read attached document
Should not have
• read attached document

```html
<!DOCTYPE html>
<html lang="en">
<head>
<meta charset="utf-8">
<title>Velora – Well Being Through Smart Research</title>
<link rel="stylesheet" href="https://fonts.googleapis.com/css2?family=Raleway:wght@400;500;600;700&display=swap">
<style>
:root{
  --teal:#1bb7bd;
  --footer:#17b5bd;
  --blue:#0255a3;
  --purple:#a54499;
  --green:#9bcb3c;
  --olive:#b5c27a;
  --ink:#222;
  --white:#fff;
}
*{box-sizing:border-box;margin:0;padding:0}
html,body{width:1200px;height:2949px;overflow:hidden}
body{position:relative;background:var(--white);font-family:"Raleway",sans-serif;color:var(--ink)}
a{text-decoration:none}
.abs{position:absolute}
/* header */
.brand{left:58px;top:14px;width:130px;text-align:center}
.brand-mark{display:block;width:50px;height:50px;border:3px solid var(--teal);border-radius:50%;margin:0 auto 6px}
.brand-name{font-weight:700;font-size:26px;letter-spacing:3px;color:#1a1a1a}
.main-nav{left:540px;top:64px;display:flex;gap:34px;font-size:17px;font-weight:500}
.main-nav a{color:var(--teal);padding-bottom:6px}
.main-nav a.current{border-bottom:3px solid var(--purple)}
.main-nav a.hover{color:var(--green)}
.search{left:834px;top:18px;width:36px;height:36px;border:2px solid var(--teal);border-radius:50%}
.langs{left:985px;top:22px;display:flex;gap:9px}
.langs span{width:26px;height:26px;border-radius:50%;background:#d8dde3;display:block}
/* hero */
.hero-image{left:26px;top:118px;width:1174px;height:455px;background:linear-gradient(100deg,#f3eeea 0%,#f7f7f7 40%,#f4f7f7 60%,#eef0e6 85%,#e9ece0 100%)}
.hero-title{left:0;width:1200px;top:368px;text-align:center;font-size:28px;font-weight:600;letter-spacing:1px;color:var(--teal)}
.btn-outline,.btn-fill{height:46px;border-radius:8px;font-size:15px;font-weight:600;letter-spacing:1px;display:flex;align-items:center;justify-content:center}
.btn-outline{left:397px;top:511px;width:174px;border:2px solid var(--purple);color:var(--purple);background:#fff}
.btn-fill{left:627px;top:511px;width:178px;background:var(--purple);color:#fff}
/* sections */
.section-title{left:0;width:1200px;text-align:center;font-size:27px;font-weight:500;color:var(--blue)}
.about-text{left:148px;top:714px;width:905px;text-align:center;font-size:17.5px;line-height:26px;font-weight:500;letter-spacing:.5px;color:#222}
/* categories */
.cat{display:flex;align-items:center;justify-content:center;font-size:16px;font-weight:600;color:#29e0e8}
.cat-nutrition{left:43px;top:1115px;width:266px;height:213px;background:linear-gradient(160deg,#f3a23a,#f6e2b4 55%,#e9ecef)}
.cat-dietary{left:346px;top:1078px;width:512px;height:263px;background:linear-gradient(150deg,#9fd03a,#c6e36e 45%,#eee 75%);box-shadow:4px 5px 8px rgba(0,0,0,.35);font-size:20px}
.cat-sport{left:860px;top:1115px;width:297px;height:213px;background:linear-gradient(160deg,#9ab1c6,#32457a 55%,#c9d3de)}
.cat-rule{left:87px;top:1346px}
/* products */
.bottle{width:140px;height:212px;border-radius:14px 14px 6px 6px;background:linear-gradient(#cfd3d6 0 16%,#fbfbfb 16% 62%,#f1f3f4 62%)}
.bottle.green{box-shadow:inset 0 -40px 0 -34px #3aa66b}
.bottle.blue{box-shadow:inset 0 -40px 0 -34px #2e7fc9}
.bottle.teal{box-shadow:inset 0 -40px 0 -34px #2aa58f}
.product-text{width:300px;text-align:center;font-size:14.5px;line-height:21px;font-weight:500}
.btn-product{width:173px;height:42px;border-radius:8px;background:var(--teal);color:#fff;font-size:13.5px;font-weight:600;line-height:16px;text-align:center;display:flex;flex-direction:column;justify-content:center}
/* blog */
.blog-img{top:2032px;width:343px;height:226px;border-radius:8px}
.blog-meta{top:2273px;font-size:12px;color:#555;display:flex;justify-content:space-between;width:303px}
.blog-meta .comments{display:flex;align-items:center;gap:8px}
.blog-rule{top:2325px;width:257px;height:2px;background:#ddd}
.blog-title{top:2350px;width:343px;text-align:center;font-size:17px;font-weight:500;letter-spacing:.5px}
.blog-text{top:2398px;width:245px;text-align:center;font-size:13px;line-height:23px;letter-spacing:.3px;color:#333}
.btn-read{top:2533px;width:130px;height:30px;border-radius:8px;background:var(--teal);color:#fff;font-size:13px;font-weight:600;display:flex;align-items:center;justify-content:center}
/* footer */
.footer{left:0;top:2734px;width:1200px;height:215px;background:var(--footer);color:#fff}
.footer-brand{left:40px;top:48px;width:180px;text-align:center}
.footer-brand .brand-mark{width:74px;height:74px;border-color:#111}
.footer-brand .brand-name{font-size:33px;color:#111}
.footer-nav{left:425px;top:40px;display:flex;gap:15px;font-size:14px;font-weight:600}
.social{top:118px;width:44px;height:44px;border-radius:50%;background:#fff}
.copyright{left:0;width:1200px;top:200px;text-align:center;font-size:10px}
.company{left:915px;top:20px;font-size:14px;font-weight:700}
.contact-line{left:900px;display:flex;gap:12px;font-size:13px;font-weight:500;line-height:18px}
.contact-line svg{flex:none}
</style>
</head>
<body>

<header>
  <div class="abs brand"><span class="brand-mark"></span><span class="brand-name">VELORA</span></div>
  <nav class="abs main-nav">
    <a class="current">Home</a><a class="hover">Products</a><a>Blog</a><a>Contact Us</a>
  </nav>
  <svg class="abs search" viewBox="0 0 36 36"><circle cx="16" cy="16" r="6" fill="none" stroke="#1bb7bd" stroke-width="2"/><line x1="20.5" y1="20.5" x2="25" y2="25" stroke="#1bb7bd" stroke-width="2"/></svg>
  <div class="abs langs" aria-label="Language choice"><span></span><span></span><span></span><span></span><span></span></div>
</header>

<section class="hero">
  <div class="abs hero-image" role="img" aria-label="Hero photo: supplement sachet poured into a glass of water, with sachets, capsules and a circle of fresh food"></div>
  <h1 class="abs hero-title">WELL BEING THROUGH SMART RESEARCH</h1>
  <a class="abs btn-outline">LEARN MORE</a>
  <a class="abs btn-fill">ORDER NOW</a>
</section>

<section class="about">
  <h2 class="abs section-title" style="top:660px">About Us</h2>
  <p class="abs about-text">Lorem ipsum dolor sit amet, consectetuer adipiscing elit. Aenean commodo ligula eget dolor. Aenean massa. Cum sociis natoque penatibus et magnis dis parturient montes, nascetur ridiculus mus. Donec quam felis, ultricies nec, pellentesque eu, pretium quis, sem. Nulla consequat massa quis enim. Donec pede justo, fringilla vel, aliquet nec, vulputate eget, arcu.</p>
</section>

<section class="products">
  <h2 class="abs section-title" style="top:934px">Products</h2>
  <div class="abs cat cat-nutrition" role="img" aria-label="Fruit, juice and tablets">Nutrition Supplement</div>
  <div class="abs cat cat-sport" role="img" aria-label="Dumbbells and supplement bottles">Sport Supplement</div>
  <div class="abs cat cat-dietary" role="img" aria-label="Measuring tape and colourful pills">Dietry Supplement</div>
  <svg class="abs cat-rule" width="1026" height="30"><path d="M0 21H498L513 7 528 21H1026" fill="none" stroke="#b5c27a" stroke-width="2"/></svg>

  <div class="abs bottle green" style="left:142px;top:1406px" role="img" aria-label="CalmaMono supplement bottle"></div>
  <div class="abs bottle blue" style="left:530px;top:1406px" role="img" aria-label="B Vita supplement bottle"></div>
  <div class="abs bottle teal" style="left:910px;top:1406px" role="img" aria-label="FloraGink supplement bottle"></div>

  <p class="abs product-text" style="left:62px;top:1684px">Lorem ipsum dolor sit amet,<br>consectetuer adipiscing elit.</p>
  <p class="abs product-text" style="left:450px;top:1684px">Lorem ipsum dolor sit amet,<br>consectetuer adipiscing elit.</p>
  <p class="abs product-text" style="left:830px;top:1684px">Lorem ipsum dolor sit amet,<br>consectetuer adipiscing elit.</p>

  <a class="abs btn-product" style="left:137px;top:1753px">View Detail<br>Place Order</a>
  <a class="abs btn-product" style="left:505px;top:1753px">View Detail<br>Place Order</a>
  <a class="abs btn-product" style="left:872px;top:1753px">View Detail<br>Place Order</a>
</section>

<section class="blog">
  <h2 class="abs section-title" style="top:1912px">Our Recent Blog Posts</h2>

  <div class="abs blog-img" style="left:43px;background:linear-gradient(135deg,#6c8f3a,#c9a870 55%,#eadfc6)" role="img" aria-label="Herbal capsules in a glass bowl"></div>
  <div class="abs blog-img" style="left:429px;background:linear-gradient(135deg,#eef3f8,#b7c9dc)" role="img" aria-label="Fork with colourful pills on a plate"></div>
  <div class="abs blog-img" style="left:812px;background:linear-gradient(135deg,#e9c29c,#f4e5d6 55%,#d99b3e);border:2px solid var(--teal)" role="img" aria-label="Waist with measuring tape and capsules"></div>

  <div class="abs blog-meta" style="left:62px"><span>August 29, 2014</span><span class="comments"><svg width="26" height="20"><path d="M2 2H24V14H10L5 18V14H2Z" fill="none" stroke="#888" stroke-width="1.5"/></svg>No Comments</span></div>
  <div class="abs blog-meta" style="left:440px"><span>August 29, 2014</span><span class="comments"><svg width="26" height="20"><path d="M2 2H24V14H10L5 18V14H2Z" fill="none" stroke="#888" stroke-width="1.5"/></svg>5 Comments</span></div>
  <div class="abs blog-meta" style="left:830px"><span>August 29, 2014</span><span class="comments"><svg width="26" height="20"><path d="M2 2H24V14H10L5 18V14H2Z" fill="none" stroke="#888" stroke-width="1.5"/></svg>12 Comments</span></div>

  <div class="abs blog-rule" style="left:87px"></div>
  <div class="abs blog-rule" style="left:472px"></div>
  <div class="abs blog-rule" style="left:855px"></div>

  <h3 class="abs blog-title" style="left:43px">Smart Living</h3>
  <h3 class="abs blog-title" style="left:429px">Smart Dieting</h3>
  <h3 class="abs blog-title" style="left:812px">Smart Body</h3>

  <p class="abs blog-text" style="left:93px">Lorem ipsum dolor sit amet, consectetuer adipiscing elit. Aenean commodo ligula eget dolor. Aenean massa. Cum sociis natoque penatibus et magnis dis parturient montes, nascetur ridiculus mus [...]</p>
  <p class="abs blog-text" style="left:478px">Lorem ipsum dolor sit amet, consectetuer adipiscing elit. Aenean commodo ligula eget dolor. Aenean massa. Cum sociis natoque penatibus et magnis dis parturient montes, nascetur ridiculus mus [...]</p>
  <p class="abs blog-text" style="left:861px">Lorem ipsum dolor sit amet, consectetuer adipiscing elit. Aenean commodo ligula eget dolor. Aenean massa. Cum sociis natoque penatibus et magnis dis parturient montes, nascetur ridiculus mus [...]</p>

  <a class="abs btn-read" style="left:149px">Read More...</a>
  <a class="abs btn-read" style="left:528px">Read More...</a>
  <a class="abs btn-read" style="left:914px">Read More...</a>
</section>

<footer class="abs footer">
  <div class="abs footer-brand"><span class="brand-mark"></span><span class="brand-name">VELORA</span></div>
  <nav class="abs footer-nav"><span>Home</span><span>Blog</span><span>Products</span><span>About Us</span><span>Contact Us</span></nav>
  <span class="abs social" style="left:480px"></span>
  <span class="abs social" style="left:568px"></span>
  <span class="abs social" style="left:661px"></span>
  <p class="abs copyright">© 2017 - VELORA - All rights reserved</p>

  <p class="abs company">Verdant Nutrition Research GmbH</p>
  <div class="abs contact-line" style="top:46px">
    <svg width="18" height="24" viewBox="0 0 18 24"><path d="M9 23C9 23 1 13 1 8.5A8 8 0 0 1 17 8.5C17 13 9 23 9 23Z" fill="#fff"/><circle cx="9" cy="8.5" r="3" fill="#17b5bd"/></svg>
    <span style="text-align:center">Lindenweg 14/b/2<br>8020 Talheim<br>Austria</span>
  </div>
  <div class="abs contact-line" style="top:120px;align-items:center">
    <svg width="20" height="20" viewBox="0 0 20 20"><path d="M4 1L8 5 6 8C7.5 11 9 12.5 12 14L15 12 19 16 16 19C8 18 2 12 1 4Z" fill="#fff"/></svg>
    <span>+43 6800 000123</span>
  </div>
  <div class="abs contact-line" style="top:162px;align-items:center">
    <svg width="20" height="20" viewBox="0 0 20 20"><circle cx="10" cy="10" r="4" fill="none" stroke="#fff" stroke-width="2.4"/><path d="M14 6V12C14 14 18 14 18 10A8 8 0 1 0 13 17.5" fill="none" stroke="#fff" stroke-width="2.4"/></svg>
    <span>m.weber@verdantnutrition.example</span>
  </div>
</footer>

</body>
</html>
```